Promotional poster for a vintage motorcycle show.

Vertically oriented, based on 11 x 17 inch proportions

Though not to the exclusion of other design concepts, stylistically perhaps something evoking a vintage (early-mid 20th century) 2-3 color silk screen style event poster.

In addition to some sort of eyecatching, vintage / antique motorbike oriented graphic (preferably not Corwin Baxley based), the poster should include the following text and info:

3rd Annual Milo Quenby Vintage Motorcycle Show
Bordentown City, N.J.
October 1st (rain date Oct. 2nd)
11am-4pm

Presented in conjunction with the 27th Annual Thistlewood Fair

For further info, or to register your pre-1992 bike contact:
Marty@wheelvaultex.com or 555-204-8913

Sponsored by:
UptownHallowmereGuildway.com
Wheelvaultex.com

Must have
• See above project description
Nice to have
• See above project describtion

```html
<!DOCTYPE html>
<html lang="en">
<head>
<meta charset="utf-8">
<title>Vintage Motorcycle Show Poster</title>
<link href="https://fonts.googleapis.com/css2?family=IM+Fell+Double+Pica+SC&family=IM+Fell+English&display=swap" rel="stylesheet">
<style>
  :root {
    --page-bg: #d9d6d1;
    --wood-dark: #3a1408;
    --wood-mid: #6b2710;
    --wood-light: #8a3a1a;
    --paper-light: #f0b24a;
    --paper-mid: #d17a22;
    --paper-dark: #8a3810;
    --burn: #2a0c04;
    --ink: #2b1206;
    --rule: #5a2a10;
    --art-light: #6a3412;
    --art-dark: #3a1808;
  }
  * { margin: 0; padding: 0; box-sizing: border-box; }
  html, body { width: 1200px; height: 1200px; overflow: hidden; background: var(--page-bg); }
  .poster {
    position: absolute; left: 210px; top: 28px; width: 780px; height: 1144px;
    background:
      repeating-linear-gradient(180deg, transparent 0 120px, rgba(0,0,0,.35) 120px 124px),
      linear-gradient(90deg, var(--wood-dark), var(--wood-mid) 20%, var(--wood-light) 50%, var(--wood-mid) 80%, var(--wood-dark));
    overflow: hidden;
  }
  .parchment { position: absolute; left: 0; top: 0; width: 780px; height: 1144px; }
  .copy {
    position: absolute; left: 0; width: 780px; text-align: center; color: var(--ink);
    font-family: "IM Fell English", Georgia, serif;
  }
  .kicker { top: 112px; font-size: 32px; line-height: 40px; font-weight: 700; }
  .title {
    top: 158px;
    font-family: "IM Fell Double Pica SC", Georgia, serif;
    font-size: 64px; line-height: 62px; letter-spacing: 1px; font-weight: 400;
  }
  .location { top: 352px; font-size: 34px; line-height: 40px; font-weight: 700; }
  .rule { position: absolute; left: 120px; width: 540px; height: 2px; background: var(--rule); opacity: .7; }
  .rule-top { top: 406px; }
  .date { top: 420px; font-size: 36px; line-height: 44px; font-weight: 700; }
  .artwork {
    position: absolute; left: 110px; top: 574px; width: 560px; height: 190px;
    border-radius: 24px;
    background: linear-gradient(180deg, var(--art-light), var(--art-dark));
    opacity: .85;
  }
  .details { top: 786px; font-size: 21px; line-height: 28px; font-weight: 700; }
  .rule-bottom { top: 942px; }
  .sponsors-label { top: 954px; font-size: 27px; line-height: 34px; font-weight: 700; }
  .sponsors { top: 996px; font-size: 20px; line-height: 28px; font-weight: 700; letter-spacing: .5px; }
</style>
</head>
<body>
  <main class="poster">
    <svg class="parchment" viewBox="0 0 780 1144" aria-hidden="true">
      <defs>
        <radialGradient id="paperGlow" cx="50%" cy="40%" r="65%">
          <stop offset="0%" stop-color="#f5c25a"/>
          <stop offset="55%" stop-color="#d9862a"/>
          <stop offset="100%" stop-color="#8a3810"/>
        </radialGradient>
      </defs>
      <path d="M40 92 L120 82 L260 88 L400 80 L560 86 L700 80 L740 92 L736 220 L746 380 L732 560 L744 740 L734 900 L742 1040 L720 1082 L560 1076 L400 1084 L240 1074 L80 1082 L46 1060 L52 900 L38 740 L50 560 L36 380 L48 220 Z"
            fill="url(#paperGlow)" stroke="#2a0c04" stroke-width="8" stroke-linejoin="round"/>
      <path d="M40 92 L72 70 L96 110 Z" fill="#6b2710"/>
      <path d="M740 1040 L742 1082 L700 1082 Z" fill="#6b2710"/>
    </svg>

    <p class="copy kicker">3rd Annual Milo Quenby</p>
    <h1 class="copy title">VINTAGE<br>MOTORCYCLE<br>SHOW</h1>
    <p class="copy location">Bordentown City, N.J.</p>
    <div class="rule rule-top"></div>
    <p class="copy date">October 1st<br>(rain date Oct. 2nd)<br>11am-4pm</p>

    <div class="artwork" role="img" aria-label="Two vintage motorcycle racers leaning into a turn, facing each other"></div>

    <p class="copy details">Presented in conjunction with the 27th Annual<br>Thistlewood Fair<br>For further info, or to register<br>your pre-1992 bike contact:<br>Marty@wheelvaultex.com or 555-204-8913</p>
    <div class="rule rule-bottom"></div>
    <p class="copy sponsors-label">Sponsored by:</p>
    <p class="copy sponsors">UptownHallowmereGuildway.com<br>Wheelvaultex.com</p>
  </main>
</body>
</html>
```